Varemo Group Business Card Design

The CEO is looking for a new trendy look for his business card.
You can stay with current branding or come up with something new/creative. It can be 3D, including Medical Office buildings. You can use our logo in a variety of colors. Please include name, title, company name, company website, email address, cell number

Target Market(s)

Real Estate Development and Construction

Industry/Entity Type

Health care real estate

Contact Information for Business Card

Rohesh Kumbar, CEO M-727.418.9062 E-roheshkumbar@varemo.com Address:4100 Lindell Ave, Tampa, FL 33611 www.varemo.com

Font styles to use
Other font styles liked:
• Be creative

Requirements
Must have
• Creative, trendy look
Nice to have
• Please go to our website to get a feel- www. varemo.com
Should not have
• small fonts

```html
<!DOCTYPE html>
<html lang="en">
<head>
<meta charset="UTF-8">
<title>Varemo Group Business Card</title>
<link rel="stylesheet" href="https://fonts.googleapis.com/css2?family=Poppins:wght@400;700;800&display=swap">
<style>
  :root {
    --stage: #2b2b2b;
    --card-white: #ffffff;
    --card-black: #262626;
    --brand-red: #b01e29;
    --ink: #222222;
    --rule: #333333;
    --emboss: #3c3c3c;
  }
  * { margin: 0; padding: 0; box-sizing: border-box; }
  html, body {
    width: 1200px; height: 875px; overflow: hidden;
    background: var(--stage);
    font-family: "Poppins", sans-serif;
  }
  .stage {
    width: 1200px; height: 875px;
    display: flex; align-items: center; justify-content: center; gap: 44px;
  }
  .card {
    width: 520px; height: 298px;
    border-radius: 22px;
    position: relative;
    box-shadow: 0 18px 40px rgba(0,0,0,0.45);
  }
  .card-front {
    background: var(--card-white);
    display: flex; align-items: center;
  }
  .front-brand {
    width: 238px;
    display: flex; justify-content: center;
    padding-left: 22px;
  }
  .brand-name {
    color: var(--brand-red);
    font-weight: 800;
    font-size: 34px;
    line-height: 1.02;
    letter-spacing: -0.5px;
  }
  .divider {
    width: 1.5px; height: 124px;
    background: var(--rule);
    margin: 0 22px 0 10px;
  }
  .contact { color: var(--ink); font-size: 12.5px; line-height: 1.42; }
  .contact-name {
    color: var(--brand-red);
    font-weight: 700; font-size: 20px; line-height: 1.1;
  }
  .contact-title { margin-bottom: 2px; }
  .contact-address { margin-bottom: 2px; }
  .contact-line { display: flex; align-items: center; gap: 7px; }
  .contact-line svg { width: 10px; height: 10px; flex: none; fill: var(--brand-red); }
  .card-back {
    background: var(--card-black);
    display: flex; align-items: center; justify-content: center;
  }
  .back-brand {
    color: var(--emboss);
    font-weight: 800;
    font-size: 52px;
    line-height: 1;
    letter-spacing: -1px;
    text-align: center;
  }
</style>
</head>
<body>
<main class="stage">
  <section class="card card-front" aria-label="Business card front">
    <div class="front-brand">
      <p class="brand-name">Varemo<br>Group</p>
    </div>
    <div class="divider"></div>
    <div class="contact">
      <p class="contact-name">Rohesh Kumbar</p>
      <p class="contact-title">CEO</p>
      <p class="contact-address">4100 Lindell Ave.<br>Tampa, FL 33611</p>
      <p class="contact-line">
        <svg viewBox="0 0 10 10" aria-hidden="true"><path d="M2 0.5 L3.8 0.5 L4.3 3 L3 3.8 Q4 6 6.2 7 L7 5.7 L9.5 6.2 L9.5 8 Q9.5 9.5 8 9.5 Q0.5 9 0.5 2 Q0.5 0.5 2 0.5Z"/></svg>
        727.418.9062
      </p>
      <p class="contact-line">
        <svg viewBox="0 0 10 10" aria-hidden="true"><path d="M0.5 2 H9.5 V8.5 H0.5Z M0.5 2 L5 5.5 L9.5 2" stroke="#fff" stroke-width="0.8"/></svg>
        roheshkumbar@varemo.com
      </p>
      <p class="contact-line">
        <svg viewBox="0 0 10 10" aria-hidden="true"><circle cx="5" cy="5" r="4.5"/><path d="M0.5 5 H9.5 M5 0.5 Q2 5 5 9.5 Q8 5 5 0.5" stroke="#fff" stroke-width="0.7" fill="none"/></svg>
        www.varemo.com
      </p>
    </div>
  </section>

  <section class="card card-back" aria-label="Business card back">
    <p class="back-brand">Varemo<br>Group</p>
  </section>
</main>
</body>
</html>
```